Label/ sleeve for olive oil tin can

We are looking for a design of a full sleeve label for our olive oil cans. These cans contain 500ml of oil and the label should have a dimension of approximately 215mm wide and 175mm high.

Please find the first draft of the design guidelines attached as well as the brand logo.
Updates

Low design quality

Target Market(s)

Consumers

Industry/Entity Type

Olive oil

Colors
00AB8E
00BBA5
67D7C9
C6EFE9
E9F9F6

Requirements
Must have
• Full label design - around the entire bottle. Read the brief

```html
<!DOCTYPE html>
<html lang="en">
<head>
<meta charset="utf-8">
<title>Villa Aurelia – Extra Virgin Olive Oil Sleeve Label</title>
<link rel="stylesheet" href="https://fonts.googleapis.com/css2?family=Marcellus&family=Outfit:wght@400;500&family=Playfair+Display:ital,wght@0,700;1,400;1,700&display=swap">
<style>
  :root {
    --backdrop: #efefef;
    --olive: #646b51;
    --olive-dark: #4f563f;
    --gold: #cdb785;
    --gold-light: #efe2b8;
    --gold-deep: #a88a4e;
    --cream: #f4f0e4;
    --organic: #eadc86;
    --ink-on-gold: #5a5235;
  }
  * { box-sizing: border-box; margin: 0; padding: 0; }
  html, body { width: 1200px; height: 1200px; overflow: hidden; }
  body {
    background: var(--backdrop);
    position: relative;
    font-family: "Outfit", sans-serif;
    color: var(--cream);
  }
  .label-panel {
    position: absolute;
    top: 60px;
    width: 460px;
    height: 1080px;
    background: linear-gradient(90deg, var(--olive-dark) 0%, var(--olive) 30%, #737a5f 55%, var(--olive) 78%, var(--olive-dark) 100%);
    text-align: center;
  }
  .label-panel--front { left: 110px; }
  .label-panel--back { left: 630px; }
  .label-panel > * { position: absolute; left: 0; right: 0; }

  .villa-scene {
    top: 58px; left: 70px; right: 70px; height: 324px;
    border: 2px solid var(--gold);
    border-radius: 160px 160px 0 0;
    padding: 8px;
  }
  .villa-scene__fill {
    width: 100%; height: 100%;
    border-radius: 152px 152px 0 0;
    background: linear-gradient(180deg, var(--gold-light) 0%, var(--gold) 45%, #9a8f74 72%, #6b6b6b 100%);
  }
  .brand-name {
    font-family: "Marcellus", serif;
    font-size: 60px;
    color: var(--gold);
    letter-spacing: 1px;
    line-height: 1;
  }
  .brand-tagline { font-size: 18px; line-height: 1; }
  .label-panel--front .brand-name { top: 398px; }
  .label-panel--front .brand-tagline { top: 478px; }

  .product-title {
    top: 548px;
    font-family: "Playfair Display", serif;
    font-weight: 700;
    color: var(--gold);
    line-height: 1;
    transform: scaleX(0.86);
  }
  .product-title span { display: block; }
  .product-title .line-one { font-size: 64px; }
  .product-title .line-two { font-size: 74px; margin-top: 4px; }
  .product-title-greek { top: 708px; font-size: 25px; letter-spacing: 0.5px; }
  .organic-mark {
    top: 796px;
    font-family: "Playfair Display", serif;
    font-style: italic; font-weight: 700;
    font-size: 36px; color: var(--organic);
  }
  .origin-note {
    top: 860px;
    font-family: "Playfair Display", serif;
    font-style: italic; font-size: 20px; line-height: 32px;
  }
  .limited-edition {
    top: 938px; left: 80px; right: 80px; height: 60px;
    border-top: 2px solid var(--gold);
    border-bottom: 2px solid var(--gold);
    font-family: "Playfair Display", serif;
    font-style: italic; font-weight: 700;
    font-size: 30px; line-height: 54px;
    color: var(--gold);
  }
  .volume { top: 1012px; font-size: 24px; }
  .base-band {
    bottom: 0; height: 38px;
    background: linear-gradient(180deg, var(--gold-light), var(--gold) 60%, var(--gold-deep));
    color: var(--ink-on-gold);
    font-weight: 500; font-size: 17px; line-height: 38px;
  }

  .label-panel--back .brand-name { top: 84px; }
  .label-panel--back .brand-tagline { top: 160px; }
  .quality-statement {
    top: 226px; left: 34px; right: 34px;
    font-family: "Playfair Display", serif;
    font-style: italic; font-size: 22px; line-height: 32px;
  }
  .badge-row, .flag-row {
    display: flex; justify-content: center; align-items: center; gap: 40px;
  }
  .badge-row { top: 462px; height: 100px; }
  .badge { border: 3px solid var(--gold); }
  .badge--square { width: 108px; height: 82px; border-radius: 12px; }
  .badge--round { width: 96px; height: 96px; border-radius: 50%; }
  .flag-row { top: 606px; height: 66px; gap: 22px; }
  .flag-shape { height: 64px; }
  .flag-shape--blue { width: 110px; background: #3f78c4; }
  .flag-shape--navy { width: 130px; background: #3a4fa0; }
  .flag-shape--round { width: 52px; height: 52px; border-radius: 50%; background: #f4f4f4; }
  .acidity { top: 700px; font-size: 24px; line-height: 30px; }
  .acidity strong { font-weight: 500; display: block; }
  .storage { top: 790px; font-size: 24px; font-weight: 500; line-height: 31px; }
  .producer { top: 912px; font-size: 24px; line-height: 29px; }
  .label-panel--back .base-band { height: 34px; }
</style>
</head>
<body>
  <section class="label-panel label-panel--front">
    <div class="villa-scene">
      <div class="villa-scene__fill" role="img" aria-label="Illustration of the villa pavilion under a white sun, flanked by olive trees"></div>
    </div>
    <h1 class="brand-name">Villa Aurelia</h1>
    <p class="brand-tagline">Holiday Rental &amp; Extra-Virgin Olive Oil</p>
    <h2 class="product-title"><span class="line-one">EXTRA VIRGIN</span><span class="line-two">OLIVE OIL</span></h2>
    <p class="product-title-greek">ΕΞΤΡΑ ΠΑΡΘΕΝΟ ΕΛΑΙΟΛΑΔΟ</p>
    <p class="organic-mark">· Organic ·</p>
    <p class="origin-note">From Villa Aurelia’s olive trees on<br>Zakynthos island</p>
    <p class="limited-edition">Limited Production</p>
    <p class="volume">0.5 Lt</p>
    <p class="base-band">FIRST COLD PRESSING | ΠΡΩΤΟ ΨΥΧΡΟ ΠΙΕΣΗ</p>
  </section>

  <section class="label-panel label-panel--back">
    <h2 class="brand-name">Villa Aurelia</h2>
    <p class="brand-tagline">Holiday Rental &amp; Extra-Virgin Olive Oil</p>
    <p class="quality-statement">Superior category olive oil obtained directly from olives and solely by mechanical means. Ελαιόλαδο ανώτερης κατηγορίας που λαμβάνεται απευθείας από ελιές και αποκλειστικά με μηχανικά μέσα.</p>
    <div class="badge-row">
      <div class="badge badge--square" role="img" aria-label="Luggage-safe packaging badge"></div>
      <div class="badge badge--round" role="img" aria-label="Organic certification badge"></div>
    </div>
    <div class="flag-row">
      <div class="flag-shape flag-shape--blue" role="img" aria-label="Flag of Greece"></div>
      <div class="flag-shape flag-shape--navy" role="img" aria-label="Flag of the European Union"></div>
      <div class="flag-shape flag-shape--round" role="img" aria-label="Recycling symbol"></div>
    </div>
    <p class="acidity"><strong>ACIDITY:</strong>max 0.8%, Οξύτητα: μέγιστο 0,8%</p>
    <p class="storage">KEEP IN DRY &amp; COLD PLACE (&lt;25 °C)<br>ΔΙΑΤΗΡΕΙΤΑΙ ΣΕ ΞΗΡΟ ΚΑΙ ΚΡΥΟ<br>ΜΕΡΟΣ (&lt;25 °C)</p>
    <p class="producer">Produced &amp; bottled at<br>Villa Aurelia<br>Greece, Zakynthos, Porto Lefki<br>www.villaaurelia-example.com</p>
    <div class="base-band"></div>
  </section>
</body>
</html>
```